DESSERT FLYER

We need a flyer design for desserts and drinks for our restaurant.

We use Retro/rustic as main theme

Flyer must include all images, which are attached to this project. We also named correctly for each images, so you can use for each dish's title (docx file)
Must include our logo as well.

Flyer tittle is "SWEET PLUMO"

Please see our website for reference at brickhollow.com.au

Flyer's printing size is A5 Vertical. Single Side

```html
<!DOCTYPE html>
<html lang="en">
<head>
<meta charset="utf-8">
<title>Sweet Plumo – Brick Hollow Dessert Menu</title>
<link rel="stylesheet" href="https://fonts.googleapis.com/css2?family=Alfa+Slab+One&family=Playfair+Display:ital,wght@1,900&display=swap">
<style>
  :root {
    --wood-dark: #1c1b1a;
    --wood-mid: #2e2c2a;
    --wood-light: #3a3835;
    --frame: #f2f2f2;
    --band-light: #e0e0e0;
    --band-dark: #b9b9b9;
    --ink: #111111;
    --paper: #ffffff;
    --price: #f3c21a;
    --brand: #27a89a;
  }
  * { margin: 0; padding: 0; box-sizing: border-box; }
  html, body { width: 846px; height: 1200px; overflow: hidden; background: var(--wood-dark); }
  .flyer {
    position: relative;
    width: 846px; height: 1200px;
    background:
      repeating-linear-gradient(90deg, rgba(255,255,255,0.03) 0 3px, transparent 3px 38px),
      linear-gradient(180deg, var(--wood-mid), var(--wood-dark) 45%, var(--wood-light) 100%);
    font-family: "Alfa Slab One", Georgia, serif;
    overflow: hidden;
  }
  .frame {
    position: absolute; inset: 16px;
    border: 3px solid var(--frame);
  }
  .brand {
    position: absolute; left: 44px; top: 26px;
    color: var(--brand);
    font-size: 38px; line-height: 1;
    letter-spacing: 1px;
  }
  .brand span { display: block; }
  .title {
    position: absolute; left: 292px; top: 56px; width: 490px;
    color: var(--paper);
    font-size: 58px; line-height: 1;
    letter-spacing: 1px; text-align: center; white-space: nowrap;
  }
  .band {
    position: absolute; left: 70px; width: 706px; height: 141px;
    background: linear-gradient(90deg, var(--band-dark), var(--band-light) 60%, var(--band-dark));
  }
  .photo {
    position: absolute; width: 272px; height: 141px;
  }
  .photo--left { left: 70px; }
  .photo--right { left: 500px; }
  .dish {
    position: absolute;
    text-align: center;
    font-size: 22px; line-height: 1.2;
    text-transform: uppercase;
  }
  .dish--on-band { left: 342px; width: 434px; color: var(--ink); }
  .dish--on-wood { left: 70px; width: 420px; color: var(--paper); }
  .dish small { font-size: 18px; display: block; }
  .price {
    display: block;
    font-family: "Playfair Display", Georgia, serif;
    font-style: italic; font-weight: 900;
    font-size: 24px; text-transform: none;
  }
  .dish--on-band .price { color: var(--ink); }
  .dish--on-wood .price { color: var(--price); }
</style>
</head>
<body>
<main class="flyer">
  <div class="frame"></div>

  <div class="brand"><span>BRICK</span><span>HOLLOW</span></div>
  <h1 class="title">SWEET PLUMO</h1>

  <!-- Row 1 -->
  <div class="band" style="top:171px"></div>
  <div class="photo photo--left" style="top:171px;background:linear-gradient(135deg,#7a2a18,#c9b48a 55%,#5a1e12)" role="img" aria-label="Fresh young coconut with straw on a table"></div>
  <p class="dish dish--on-band" style="top:206px">Fresh Young<br>Coconut Juice<span class="price">$5.50</span></p>

  <!-- Row 2 -->
  <p class="dish dish--on-wood" style="top:358px">Banana Fritter With<br>Vanilla Ice-Cream<span class="price">$6.90</span></p>
  <div class="photo photo--right" style="top:332px;background:linear-gradient(135deg,#2f7a1e,#d08a2a 45%,#e0a040 65%,#2f7a1e)" role="img" aria-label="Golden banana fritters on a banana leaf"></div>

  <!-- Row 3 -->
  <div class="band" style="top:500px"></div>
  <div class="photo photo--left" style="top:500px;background:linear-gradient(90deg,#3c2a4a,#6a4f7a 45%,#f2c23a 60%,#e8b030)" role="img" aria-label="Black sticky rice with sliced mango"></div>
  <p class="dish dish--on-band" style="top:530px">Black Sticky Rice<br>With Mango<span class="price">$6.90</span></p>

  <!-- Row 4 -->
  <p class="dish dish--on-wood" style="top:690px">Banana Sago Pudding With<br>Peanut Topping<span class="price">$6.90</span></p>
  <div class="photo photo--right" style="top:661px;background:linear-gradient(135deg,#2f8a22,#eef0ea 45%,#f4f4f0 60%,#3a9a2a)" role="img" aria-label="Banana sago pudding slice on a banana leaf"></div>

  <!-- Row 5 -->
  <div class="band" style="top:822px"></div>
  <div class="photo photo--left" style="top:822px;background:linear-gradient(135deg,#1e5a6a,#f0e4d0 45%,#d87a3a 65%,#1c3a4a)" role="img" aria-label="Fried ice-cream with caramel topping in a glass bowl"></div>
  <p class="dish dish--on-band" style="top:834px">Fried Ice-Cream With<br><small>Caramel/Chocolate/<br>Strawberry Topping</small><span class="price">$6.90</span></p>

  <!-- Row 6 -->
  <p class="dish dish--on-wood" style="top:1012px">Vietnamese<br>Coffee<span class="price">$6.90</span></p>
  <div class="photo photo--right" style="top:987px;background:linear-gradient(135deg,#f2e8da,#9a6a3a 45%,#3a2414 80%)" role="img" aria-label="Vietnamese drip coffee filter with coffee beans"></div>
</main>
</body>
</html>
```